Android Payment Application UI Design

We require a UI/UX design for an existing Android card-based payment application.

We're looking to improve the look + feel of the existing app. What we're after:
- Colour palette options
- Fonts
- Icons

See attached document for existing screen types, icons, etc.

All resources provided must be royalty free.

It's to run on a specialised device, with 720 x 1280 pixel resolution, in portrait only (landscape not required).

Please provide mockup examples of the new screen layout applied to the existing screens in the document.

Target Market(s)

Retail business users

Font styles to use
Sans Serif

Colors

Designer to choose colors to be used in the design.

Requirements
Must have
• Looking for
• - modern design
• - simple colours, easy-to-read sans-serif fonts
• - cohesive, consistent design between screens

```html
<!DOCTYPE html>
<html lang="en">
<head>
<meta charset="utf-8">
<title>Sale – Card Entry</title>
<link rel="stylesheet" href="https://fonts.googleapis.com/css2?family=Montserrat:wght@500;600;700&family=Roboto:wght@400;500&display=swap">
<style>
:root{
  --status-top:#10245a;
  --status-bottom:#2f6fc4;
  --header-bg:#ffffff;
  --ink:#1f2547;
  --ink-soft:#3a4060;
  --icon:#4a5060;
  --brand:#1f6fbf;
  --body-top:#ffffff;
  --body-bottom:#bfe0f3;
  --field-border:#c9d6e2;
  --placeholder:#7a7f8c;
  --pad-top:#2b9be0;
  --pad-bottom:#1480cf;
  --key-top:#ffffff;
  --key-bottom:#dcdcdc;
  --key-text:#333a48;
  --cancel:#e8322d;
  --del:#f59d25;
  --done:#4f9e1f;
}
*{box-sizing:border-box;margin:0;padding:0}
html,body{width:675px;height:1200px;overflow:hidden}
body{font-family:"Roboto",Arial,sans-serif;background:var(--body-top);position:relative}
.status-bar{position:absolute;left:0;top:0;width:675px;height:58px;
  background:linear-gradient(var(--status-top),var(--status-bottom));color:#fff;
  font-size:21px;display:flex;align-items:center;padding:0 16px}
.status-bar .signal{letter-spacing:1px;font-size:16px}
.status-bar .carrier{margin-left:10px}
.status-bar .time{position:absolute;left:0;right:0;text-align:center;pointer-events:none}
.status-bar .battery{margin-left:auto;display:flex;align-items:center;gap:8px}
.app-header{position:absolute;left:0;top:58px;width:675px;height:122px;background:var(--header-bg);
  border-bottom:1px solid #e6ebef}
.app-header .menu-left{position:absolute;left:12px;top:42px}
.app-header .menu-right{position:absolute;right:16px;top:44px}
.brand{position:absolute;left:0;right:0;top:36px;display:flex;justify-content:center;align-items:center;gap:14px}
.brand .mark{width:34px;height:34px;border-radius:50%;background:var(--brand)}
.brand .name{font-family:"Montserrat",Arial,sans-serif;font-weight:700;font-size:44px;color:var(--brand);letter-spacing:2px}
.entry{position:absolute;left:0;top:181px;width:675px;height:611px;
  background:linear-gradient(var(--body-top) 0%,var(--body-top) 20%,var(--body-bottom) 100%)}
.title{position:absolute;left:0;right:0;text-align:center;font-family:"Montserrat",Arial,sans-serif;color:var(--ink)}
.title.main{top:140px;font-size:42px;font-weight:600}
.title.sub{top:197px;font-size:34px;font-weight:600}
.field{position:absolute;background:#fff;border:1px solid var(--field-border);border-radius:14px;
  display:flex;align-items:center;color:var(--placeholder)}
.card-number{left:85px;top:287px;width:493px;height:88px;padding-left:28px;font-size:18px}
.expiry-label{position:absolute;left:85px;top:414px;font-family:"Montserrat",Arial,sans-serif;font-weight:600;font-size:26px;color:var(--ink-soft)}
.expiry-date{left:405px;top:399px;width:173px;height:62px;justify-content:center;font-size:19px;color:var(--ink-soft)}
.keypad{position:absolute;left:0;top:792px;width:675px;height:408px;
  background:linear-gradient(var(--pad-top),var(--pad-bottom));border-radius:26px 26px 0 0}
.key{position:absolute;display:flex;align-items:center;justify-content:center;
  background:linear-gradient(var(--key-top),var(--key-bottom));color:var(--key-text);
  font-size:30px;box-shadow:0 3px 4px rgba(0,0,0,.25)}
.key.action{color:#fff;font-family:"Montserrat",Arial,sans-serif;font-weight:500;font-size:19px}
.key.cancel{background:var(--cancel)}
.key.del{background:var(--del)}
.key.done{background:var(--done);font-weight:600}
</style>
</head>
<body>
<div class="status-bar">
  <span class="signal">●●●●○</span><span class="carrier">Carrier</span>
  <span class="time">11:49 AM</span>
  <span class="battery">2%
    <svg width="42" height="20" viewBox="0 0 42 20"><rect x="1" y="1" width="36" height="18" rx="3" fill="none" stroke="#fff" stroke-width="2"/><rect x="38" y="6" width="3" height="8" fill="#fff"/><rect x="4" y="4" width="3" height="12" fill="#e8322d"/></svg>
  </span>
</div>

<header class="app-header">
  <svg class="menu-left" width="26" height="34" viewBox="0 0 26 34" fill="var(--icon)">
    <ellipse cx="13" cy="5" rx="11" ry="4"/><rect x="2" y="10" width="22" height="6" rx="3"/><rect x="2" y="18" width="22" height="6" rx="3"/><rect x="2" y="26" width="22" height="6" rx="3"/>
  </svg>
  <div class="brand"><span class="mark"></span><span class="name">VEXA</span></div>
  <svg class="menu-right" width="30" height="28" viewBox="0 0 30 28" fill="var(--icon)">
    <circle cx="3.5" cy="4" r="3.5"/><circle cx="3.5" cy="14" r="3.5"/><circle cx="3.5" cy="24" r="3.5"/>
    <rect x="10" y="1.5" width="20" height="5" rx="1"/><rect x="10" y="11.5" width="20" height="5" rx="1"/><rect x="10" y="21.5" width="20" height="5" rx="1"/>
  </svg>
</header>

<main class="entry">
  <h1 class="title main">SALE</h1>
  <h2 class="title sub">PLEASE ENTER</h2>
  <div class="field card-number">Card Number</div>
  <div class="expiry-label">Expiry Date</div>
  <div class="field expiry-date">24/August/2018</div>
</main>

<section class="keypad">
  <div class="key" style="left:31px;top:56px;width:142px;height:57px">1</div>
  <div class="key" style="left:187px;top:56px;width:144px;height:57px">2</div>
  <div class="key" style="left:342px;top:56px;width:144px;height:57px">3</div>
  <div class="key action cancel" style="left:500px;top:56px;width:141px;height:57px">CANCEL</div>

  <div class="key" style="left:31px;top:139px;width:142px;height:59px">4</div>
  <div class="key" style="left:187px;top:139px;width:144px;height:59px">5</div>
  <div class="key" style="left:342px;top:139px;width:144px;height:59px">6</div>
  <div class="key action del" style="left:500px;top:139px;width:141px;height:59px">DEL</div>

  <div class="key" style="left:31px;top:223px;width:142px;height:58px">7</div>
  <div class="key" style="left:187px;top:223px;width:144px;height:58px">8</div>
  <div class="key" style="left:342px;top:223px;width:144px;height:58px">9</div>
  <div class="key action done" style="left:500px;top:223px;width:141px;height:142px">DONE</div>

  <div class="key" style="left:31px;top:306px;width:142px;height:59px">00</div>
  <div class="key" style="left:187px;top:306px;width:144px;height:59px">0</div>
  <div class="key" style="left:342px;top:306px;width:144px;height:59px">000</div>
</section>
</body>
</html>
```